Website design for commercial and residential security company

we're looking to see some new designs for an established company with no website.

homepage and one inner page

here is a link to the homepage content, sitemap, logo and more.
https://files.brontavel.net/share/7QxmPzLrTw2vNkdJhYcsa9eFgbUoiVwRn?view=open

call to action should be Request A Quote

if you have any questions please send them to us asap

thank you

1 page

Sans Serif

```html
<!DOCTYPE html>
<html lang="en">
<head>
<meta charset="utf-8">
<title>Keystone Watch Systems</title>
<link href="https://fonts.googleapis.com/css2?family=Fira+Sans:wght@500;600;700&family=Poppins:wght@400;500;600&display=swap" rel="stylesheet">
<style>
:root{
  --gold:#cfab3a;
  --navy:#131c28;
  --ink:#1b1f27;
  --muted:#6b6f76;
  --field:#e6e6e6;
  --line:#d5d5d5;
  --pale:#eceef1;
}
*{box-sizing:border-box;margin:0;padding:0}
html,body{width:1200px;height:4444px;overflow:hidden;background:#fff}
body{font-family:"Poppins",sans-serif;color:var(--ink);position:relative}
.abs{position:absolute}
h1,h2,h3,h4,.head{font-family:"Fira Sans",sans-serif}

.topbar{left:0;top:0;width:1200px;height:43px;background:var(--gold);color:#fff;font-size:10px;font-weight:600;display:flex;align-items:center;gap:26px;padding-left:238px}
.topbar span{display:flex;align-items:center;gap:5px}

.nav{left:0;top:43px;width:1200px;height:81px;background:var(--navy);display:flex;align-items:center;justify-content:space-between;padding:0 234px}
.brand{display:flex;align-items:center;gap:10px;color:var(--gold);font-family:"Fira Sans",sans-serif;font-weight:700;font-size:20px;letter-spacing:.5px}
.brand i{width:14px;height:14px;background:var(--gold);display:block;border-radius:50%}
.menu{display:flex;gap:30px;color:#fff;font-size:10px}
.menu b{font-weight:600}

.hero{left:0;top:124px;width:1200px;height:760px;background:linear-gradient(100deg,#f2f5fa 0%,#e6edf6 45%,#c9d9ec 100%)}
.hero-photo{left:600px;top:124px;width:600px;height:740px;background:linear-gradient(160deg,#b9cde4 0%,#1f4ea8 45%,#0b2c86 75%,#d7dee8 100%)}
.hero-curve{left:0;top:560px}
.hero-title{left:234px;top:240px;font-size:44px;line-height:50px;font-weight:700;color:var(--ink)}
.hero-copy{left:234px;top:366px;width:370px;font-size:10px;line-height:17px}
.btn{display:inline-flex;align-items:center;gap:8px;background:var(--gold);color:#fff;font-size:10px;font-weight:600}
.hero-btn{left:234px;top:419px;height:36px;padding:0 20px}

.safety{left:234px;top:638px;width:731px;height:203px;background:#fff;box-shadow:0 8px 30px rgba(20,30,50,.08);border-radius:4px;text-align:center}
.safety h2{margin-top:28px;font-size:22px;font-weight:700}
.safety p{width:470px;margin:12px auto 0;font-size:9.5px;line-height:16px;color:var(--muted)}
.badges{display:flex;justify-content:center;gap:50px;margin-top:6px}
.badge{font-size:9.5px;color:var(--muted);display:flex;flex-direction:column;align-items:center;gap:4px}

.photo{background:linear-gradient(135deg,#2b2f48,#11131f 55%,#b2284b)}
.mission-photo{left:234px;top:967px;width:294px;height:357px}
.eyebrow{color:var(--gold);font-size:12.5px;font-weight:500}
.lead{font-family:"Fira Sans",sans-serif;font-weight:600;font-size:12px;line-height:18px}
.body{font-size:9.5px;line-height:17px;color:var(--muted)}
.mission{left:609px;top:1071px;width:360px}
.mission .lead{margin-top:18px}
.mission .body{margin-top:14px}

.commercial{left:330px;top:1396px;width:540px;text-align:center}
.commercial .lead{margin-top:18px}
.commercial .body{margin-top:16px}
.commercial ul{text-align:left;margin:14px 0 0 70px;list-style:none}
.commercial li{font-size:9.5px;line-height:23px;color:var(--muted);padding-left:10px;position:relative}
.commercial li::before{content:"•";position:absolute;left:0}
.commercial .lead2{margin-top:14px;font-family:"Fira Sans",sans-serif;font-weight:600;font-size:12px;line-height:19px}

.residential{left:234px;top:2128px;width:365px}
.residential .lead{margin-top:18px}
.residential .body{margin-top:14px}
.res-btn{margin-top:16px;height:35px;padding:0 20px}
.res-photo{left:671px;top:2079px;width:294px;height:355px;background:linear-gradient(180deg,#7ea3c6,#c3d6e6 60%,#5f86ad)}

.news-dark{left:0;top:2524px;width:1200px;height:395px;background:var(--navy)}
.news-pale{left:0;top:2919px;width:1200px;height:379px;background:linear-gradient(180deg,#e8eaed,#f3f4f6)}
.news-kicker{left:234px;top:2580px;color:#fff;font-size:12px;font-weight:500}
.news-title{left:234px;top:2618px;color:#fff;font-size:22px;line-height:33px;font-weight:600}
.news-copy{left:628px;top:2618px;width:355px;color:#fff;font-size:9.5px;line-height:17px}
.card{top:2750px;width:231px;height:310px;background:#fff;padding:11px;border-radius:3px;box-shadow:0 6px 20px rgba(0,0,0,.06)}
.card-img{width:209px;height:152px;background:linear-gradient(135deg,#c7d3e0,#e9eef3)}
.card h3{margin:22px 6px 0;font-size:13px;line-height:20px;font-weight:600}
.card .more{margin:14px 6px 0;font-size:9px;font-weight:600}
.card .more.btn{padding:8px 18px}
.arrow{top:2874px;width:62px;height:62px;background:#fff;display:flex;align-items:center;justify-content:center}

.cta{left:253px;top:3210px;width:693px;height:152px;background:var(--gold);border-radius:6px}
.cta h2{position:absolute;left:63px;top:42px;color:#fff;font-size:23px;line-height:33px;font-weight:600}
.cta-btn{position:absolute;right:38px;top:56px;background:#fff;color:var(--gold);font-size:9.5px;font-weight:600;padding:11px 21px}

.contact-head{left:0;top:3465px;width:1200px;text-align:center}
.contact-head .lead{margin-top:18px}
.field{background:var(--field);border:1px solid var(--line);font-size:9.5px;color:var(--muted);padding:0 16px;display:flex;align-items:center}
.field em{color:#c0392b;font-style:normal;margin-left:3px}
.submit{left:783px;top:3836px;width:120px;height:34px;justify-content:center;font-size:9.5px}

.footer{left:0;top:3830px;width:1200px;height:549px;background:var(--navy)}
.footer-curve{left:0;top:3829px}
.foot-brand{left:248px;top:4152px}
.fcol{top:4138px;color:#fff}
.fcol h4{font-size:13px;font-weight:600;margin-bottom:18px}
.fcol p,.fcol li{font-size:9.5px;line-height:17px}
.fcol ul{list-style:none}
.fcol li{line-height:20px;display:flex;align-items:center;gap:12px}
.bottom{left:0;top:4379px;width:1200px;height:65px;background:var(--gold);color:#fff;font-size:10px;font-weight:600;display:flex;align-items:center;justify-content:center}
</style>
</head>
<body>

<div class="abs topbar">
  <span><svg width="9" height="9" viewBox="0 0 24 24" fill="#fff"><path d="M6.6 10.8a15 15 0 0 0 6.6 6.6l2.2-2.2c.3-.3.7-.4 1-.2 1.1.4 2.3.6 3.6.6.6 0 1 .4 1 1V20c0 .6-.4 1-1 1A17 17 0 0 1 3 4c0-.6.4-1 1-1h3.5c.6 0 1 .4 1 1 0 1.3.2 2.5.6 3.6.1.3 0 .7-.2 1z"/></svg>+1-202-555-0148</span>
  <span><svg width="9" height="9" viewBox="0 0 24 24"><circle cx="12" cy="12" r="10" fill="#fff"/><path d="M12 6v6l4 2" stroke="#cfab3a" stroke-width="2" fill="none"/></svg>07:00 - 16:00</span>
  <span><svg width="8" height="10" viewBox="0 0 20 26" fill="#fff"><path d="M10 0a10 10 0 0 0-10 10c0 7 10 16 10 16s10-9 10-16A10 10 0 0 0 10 0zm0 14a4 4 0 1 1 0-8 4 4 0 0 1 0 8z"/></svg>142 Alder Creek Road, Marlow GA</span>
</div>

<nav class="abs nav">
  <div class="brand"><i></i>KEYSTONE WATCH</div>
  <div class="menu"><b>Home</b><span>About</span><span>Solutions ⌄</span><span>Resources ⌄</span><span>Contact</span></div>
</nav>

<section>
  <div class="abs hero"></div>
  <div class="abs hero-photo" role="img" aria-label="Hand holding a smartphone showing a smart home security app"></div>
  <svg class="abs hero-curve" width="1200" height="330" viewBox="0 0 1200 330">
    <path d="M0 50 L232 112 L780 112 L780 280 C880 320 920 305 1000 250 L1200 110 L1200 330 L0 330Z" fill="#fff"/>
    <path d="M0 50 L232 112" stroke="#cfab3a" stroke-width="2.5" fill="none"/>
    <path d="M790 282 C880 320 925 310 1000 255 L1200 112" stroke="#cfab3a" stroke-width="9" fill="none"/>
  </svg>
  <h1 class="abs hero-title">We Ensure Security<br>with Smart Tools.</h1>
  <p class="abs hero-copy">Lorem ipsum dolor sit amet, consectetur adipiscing elit, sed do eiusmod tempor incididunt ut labore et dolore magna aliqua. Ut enim ad minim veniam.</p>
  <a class="abs btn hero-btn">Request A Quote <span>→</span></a>

  <div class="abs safety">
    <h2>SAFETY &amp; SECURITY</h2>
    <p>Lorem ipsum dolor sit amet, consectetur adipiscing elit, sed do eiusmod tempor incididunt ut labore et dolore magna aliqua. Ut enim ad minim veniam.</p>
    <div class="badges">
      <div class="badge"><svg width="44" height="48" viewBox="0 0 44 48"><path d="M22 3 L39 9 V24 C39 35 31 42 22 45 C13 42 5 35 5 24 V9Z" fill="#f2f2f2" stroke="#8a8a8a" stroke-width="2"/><path d="M14 24 l6 6 l11-12" stroke="#cfab3a" stroke-width="4" fill="none"/></svg>Security</div>
      <div class="badge"><svg width="44" height="48" viewBox="0 0 44 48"><path d="M22 3 L39 9 V24 C39 35 31 42 22 45 C13 42 5 35 5 24 V9Z" fill="#f2f2f2" stroke="#8a8a8a" stroke-width="2"/><path d="M22 11 L31 14 V24 H22Z M22 24 V37 C16 35 13 30 13 24Z" fill="#cfab3a"/></svg>Protection</div>
      <div class="badge"><svg width="44" height="48" viewBox="0 0 44 48"><path d="M22 3 L39 9 V24 C39 35 31 42 22 45 C13 42 5 35 5 24 V9Z" fill="#f2f2f2" stroke="#8a8a8a" stroke-width="2"/><g stroke="#cfab3a" stroke-width="2" fill="none"><path d="M14 30 C13 20 18 15 22 15 C27 15 31 20 30 30"/><path d="M18 33 C17 24 19 19 22 19 C25 19 27 24 26 33"/><path d="M22 23 V34"/></g></svg>Fingerprint</div>
    </div>
  </div>
</section>

<section>
  <div class="abs photo mission-photo" role="img" aria-label="Close-up of a dome security camera under red and blue light"></div>
  <div class="abs mission">
    <div class="eyebrow">Our Mission</div>
    <p class="lead">To Provide Our Customers With Comprehensive Security, Audio/Video, And Automation With Top Notch Customer Service. We Ensure Security With Smart Tools.</p>
    <p class="body">The graded security measures from Keystone Watch Systems ensure the safety of both residential and commercial property. We provide a wide range of Residential and Commercial Security Solutions.</p>
  </div>
</section>

<section class="abs commercial">
  <div class="eyebrow">Commercial Solutions</div>
  <p class="lead">Protect Assets And Security Of Your Business With Exceptional Commercial Security Installation</p>
  <p class="body">People's safety is our top priority. This includes ensuring that the security system built at your commercial property is configured accurately. Further, it will protect against intruders, burglaries, and holdups. We do this by:</p>
  <ul>
    <li>Audio &amp; Video Solutions for your commercial property</li>
    <li>Burglar Alarms &amp; Detectors</li>
    <li>CCTV cameras equipped with facial recognition technologies enable the technology to<br>identify the offenders.</li>
    <li>Monitoring of alarms and video recordings 24 hours a day, seven days a week.<br>Addressing all the incidents with an urgent response.</li>
    <li>Alarm systems and cameras precisely installed so that more of your property is tracked.</li>
  </ul>
  <p class="body">People's safety is our top priority. This includes ensuring that the security system built at your commercial property is configured accurately. Further, it will protect against intruders, burglaries, and holdups. We do this by:</p>
  <p class="lead2">We Will Help Secure Your Company Outside Of The Realm Of Conventional Monitoring Technologies. Indeed, We Take A Customised And Comprehensive Approach To Defence.</p>
  <p class="body">Flooding, smoke, power outages, temperature fluctuations, and other factors will all be tracked. So, you can take prompt steps before you experience damage.</p>
  <p class="body">But, it all comes down to internal and external security measures.</p>
  <p class="body">We can combine low-light cameras, smoke and temperature monitoring, noise control, and physical surveillance into a 24/7 commercial security solution. Thus, you can focus on running your business with utmost safety.</p>
  <p class="body">Our commercial security services are comprehensive. In fact, we have worked out how to protect companies from future threats by tailoring our strategy to each new customer. Therefore, whatever business you are into, we provide you with a security solution that physically protects you, your employees, clients, and property.</p>
</section>

<section>
  <div class="abs residential">
    <div class="eyebrow">Residential Security Solutions</div>
    <p class="lead">Consider A Home Surveillance Device That Would Do More For You And Your Family Than You Ever Imagined.</p>
    <p class="body">Keystone Watch Systems is your trustable security provider. Also, as certified professionals carry out the installation, you have everything under control. Your home is being securely watched from various points, with cameras capable of tracking any intruder's path. Specifically, we offer Residential Intrusion Detection Security Systems, Residential Alarm, Residential Network Wi-Fi, CCTVs and residential home automation.</p>
    <a class="btn res-btn">Get in touch with us today! <span>→</span></a>
  </div>
  <div class="abs res-photo" role="img" aria-label="Dome surveillance camera mounted on a pole in front of a glass office building"></div>
</section>

<section>
  <div class="abs news-dark"></div>
  <div class="abs news-pale" role="img" aria-label="Faint blueprint-style background of security equipment"></div>
  <div class="abs news-kicker">Latest News</div>
  <h2 class="abs news-title">Lorem Ipsum Dolor Sit Amet<br>Adipiscing Consectetur.</h2>
  <p class="abs news-copy">Lorem ipsum dolor sit amet, consectetur adipiscing elit, sed do eiusmod tempor incididunt ut labore et dolore magna aliqua. Ut enim ad minim veniam, quis nostrud exercitation ullamco laboris nisi ut aliquip ex ea commodo consequat duis aute irure dolor.</p>

  <div class="abs arrow" style="left:121px"><svg width="16" height="22" viewBox="0 0 16 22"><path d="M12 2 L3 11 L12 20" stroke="#111" stroke-width="3.5" fill="none"/></svg></div>
  <div class="abs arrow" style="left:1016px"><svg width="16" height="22" viewBox="0 0 16 22"><path d="M4 2 L13 11 L4 20" stroke="#111" stroke-width="3.5" fill="none"/></svg></div>

  <article class="abs card" style="left:234px">
    <div class="card-img" role="img" aria-label="Digital padlock over a glowing eye graphic"></div>
    <h3>Lorem Ipsum Dolor Sit Amet Adipiscing.</h3>
    <div class="more">Read More</div>
  </article>
  <article class="abs card" style="left:484px">
    <div class="card-img" role="img" aria-label="Paper card with a padlock icon against office towers" style="background:linear-gradient(135deg,#6f9fd6,#e8eef6)"></div>
    <h3>Lorem Ipsum Dolor Sit Amet Adipiscing.</h3>
    <div class="more btn">Read More</div>
  </article>
  <article class="abs card" style="left:734px">
    <div class="card-img" role="img" aria-label="Finger pressing a smart home button" style="background:linear-gradient(135deg,#e8e2da,#b59e86)"></div>
    <h3>Lorem Ipsum Dolor Sit Amet Adipiscing.</h3>
    <div class="more">Read More</div>
  </article>
</section>

<div class="abs cta">
  <h2>Lorem Ipsum Dolor Sit Amet,<br>Consectetur Adipiscing Elit Sed Do.</h2>
  <a class="cta-btn">Request A Quote</a>
</div>

<section>
  <div class="abs contact-head">
    <div class="eyebrow">Contact Us</div>
    <p class="lead">Lorem Ipsum Dolor Sit Amet Consectetur Adipiscing Elit Sed Do Incididunt.</p>
  </div>
  <div class="abs field" style="left:297px;top:3562px;width:294px;height:41px"></div>
  <div class="abs field" style="left:609px;top:3562px;width:294px;height:41px">Email Address<em>*</em></div>
  <div class="abs field" style="left:297px;top:3626px;width:606px;height:41px">Your Name<em>*</em></div>
  <div class="abs field" style="left:297px;top:3689px;width:606px;height:107px;align-items:flex-start;padding-top:14px">Messages<em>*</em></div>
</section>

<footer>
  <div class="abs footer"></div>
  <svg class="abs footer-curve" width="1200" height="220" viewBox="0 0 1200 220">
    <path d="M0 0 H1200 V75 C1060 120 960 205 860 205 C600 210 250 130 0 0Z" fill="#fff"/>
  </svg>
  <a class="abs btn submit">Submit Messages</a>
  <div class="abs brand foot-brand"><i></i>KEYSTONE WATCH</div>
  <div class="abs fcol" style="left:448px">
    <h4>Usefull Link</h4>
    <ul>
      <li>›<b style="font-weight:600">About Us</b></li>
      <li>›<span>Solutions</span></li>
      <li>›<span>Resources</span></li>
      <li>›<span>Contact Us</span></li>
      <li>›<span>Request A Quote</span></li>
    </ul>
  </div>
  <div class="abs fcol" style="left:582px;width:180px">
    <h4>Office</h4>
    <p>2290 Birchwood Ave. Halden,<br>Kentucky 40112<br>m.ellery@example.com<br>+1-202-555-0148</p>
  </div>
  <div class="abs fcol" style="left:797px">
    <h4>Opening Hour</h4>
    <p>Mon - Sat : 8:00 - 17:00<br>Sun : Closed</p>
  </div>
  <div class="abs bottom">Copyright © 2021. All right reserved</div>
</footer>

</body>
</html>
```